Website design for an Italian restaurant in Amsterdam

I need a design for a client of mine. It is for Teatro Lucerna, an Italian restaurant in Amsterdam.
We are going for a clean, modern look but we also need to realise an authentic feel.
The restaurant is located in an old movie theatre, that is where the name Teatro Lucerna comes from.
Industry/Entity Type
Italian Restaurant
Number of Pages Required
1 page
Font styles to use
Sans Serif
Colors
Designer to choose colors to be used in the design.

```html
<!DOCTYPE html>
<html lang="en">
<head>
<meta charset="utf-8">
<title>Italian Restaurant</title>
<link href="https://fonts.googleapis.com/css2?family=Fjalla+One&family=Lato:wght@400;700&display=swap" rel="stylesheet">
<style>
:root{
  --red:#ee1100;
  --black:#050505;
  --ink:#222;
  --muted:#555;
  --paper:#f6f6f4;
  --white:#fff;
  --line:#d9d9d9;
  --field:#f4f4f4;
}
*{box-sizing:border-box;margin:0;padding:0}
html,body{width:1200px;height:2452px;overflow:hidden}
body{position:relative;background:var(--paper);font-family:'Lato',sans-serif;color:var(--ink)}
.abs{position:absolute}
.display{font-family:'Fjalla One',sans-serif;text-transform:uppercase;letter-spacing:.5px}

.topbar{left:0;top:0;width:1200px;height:28px;background:var(--black);color:var(--white);font-size:12px}
.topbar .addr{left:190px;top:7px;display:flex;gap:8px;align-items:center}
.topbar .phone{right:190px;top:7px;display:flex;gap:10px;align-items:center}

.header{left:0;top:28px;width:1200px;height:58px;background:var(--white)}
.logo{font-family:'Fjalla One',sans-serif;font-size:28px;text-transform:uppercase;color:var(--ink)}
.header .logo{left:190px;top:12px}
.nav{right:190px;top:20px;display:flex;gap:20px;font-size:12px;color:var(--ink)}

.hero{left:0;top:86px;width:1200px;height:578px;background:linear-gradient(120deg,#2a211c 0%,#3d2f26 35%,#1c1612 70%,#2e2620 100%)}
.hero .welcome{left:190px;top:215px;color:var(--white);line-height:1}
.hero .welcome .small{font-size:38px}
.hero .welcome .big{font-size:60px;margin-top:14px}
.booking{left:654px;top:0;width:355px;height:578px;background:var(--red);color:var(--white);text-align:center}
.booking h2{font-size:36px;font-weight:400;margin-top:56px}
.booking p{font-size:11.5px;width:230px;margin:10px auto 0;line-height:1.3}
.field{width:258px;height:40px;margin:0 auto 11px;background:var(--field);border-radius:3px;color:#9a9a9a;font-size:11px;display:flex;align-items:center;padding-left:14px;text-align:left}
.field .lbl{width:44px;border-right:1px solid #ddd;height:40px;display:flex;align-items:center;margin-right:14px}
.fields{margin-top:30px}
.btn-request{width:258px;height:68px;margin:2px auto 0;background:var(--black);border-radius:3px;font-size:26px;display:flex;align-items:center;justify-content:center}

.section-title{left:0;width:1200px;display:flex;justify-content:center;align-items:center;gap:14px;font-size:38px;color:var(--black)}
.section-title::before,.section-title::after{content:"";width:58px;height:2px;background:var(--black)}

.dish{top:822px;height:329px;background:var(--white);border:2px solid var(--line);border-radius:6px;text-align:center}
.dish .plate{width:190px;height:190px;border-radius:50%;margin:20px auto 0;border:8px solid #ddd}
.dish h3{font-size:26px;font-weight:400;margin-top:26px;color:var(--black)}
.dish p{font-size:11.5px;color:var(--muted);width:200px;margin:6px auto 0;line-height:1.3}
.dish.active{background:var(--red);border-color:var(--red)}
.dish.active h3,.dish.active p{color:var(--white)}
.arrow{top:970px}

.offer{left:0;top:1261px;width:1200px;height:296px;background:radial-gradient(ellipse at 40% 40%,#3a3a3a 0%,#1e1e1e 60%,#141414 100%);color:var(--white);text-align:center}
.offer h2{font-size:38px;font-weight:400;line-height:1.25;margin-top:50px}
.offer p{font-size:11.5px;margin-top:10px}
.btn-red{display:flex;align-items:center;justify-content:center;background:var(--red);color:var(--white);border-radius:5px;font-family:'Fjalla One',sans-serif;text-transform:uppercase}
.offer .btn-red{width:202px;height:45px;margin:22px auto 0;font-size:22px}

.post{top:1694px;width:263px;height:328px;background:var(--white);border:2px solid var(--line);border-radius:6px;overflow:hidden}
.post .photo{height:170px}
.post .body{padding:18px 20px 0 20px}
.post h3{font-size:16px;font-weight:400;color:var(--black)}
.post .meta{display:flex;justify-content:space-between;font-size:11px;color:var(--muted);margin-top:6px}
.post .meta span{display:flex;gap:6px;align-items:center}
.post p{font-size:11.5px;color:var(--muted);line-height:1.3;margin-top:8px}
.post .more{font-family:'Fjalla One',sans-serif;font-size:10px;color:var(--red);margin-top:10px}
.view-more{left:499px;top:2085px;width:202px;height:45px;font-size:22px}

.footer{left:0;top:2188px;width:1200px;height:264px;background:var(--black);color:var(--white)}
.footer .logo{left:190px;top:38px;color:var(--white)}
.footer h4{font-family:'Fjalla One',sans-serif;font-weight:400;font-size:17px;color:var(--red);text-transform:uppercase;top:46px}
.footer .about{left:190px;top:90px;width:225px;font-size:11.5px;line-height:1.3}
.footer .more{left:190px;top:132px;font-family:'Fjalla One',sans-serif;font-size:10px;color:var(--red)}
.socials{left:190px;top:157px;display:flex;gap:9px}
.socials span{width:20px;height:20px;border-radius:50%;background:var(--white)}
.links{left:474px;top:88px;font-size:12px;line-height:19px}
.contact{left:601px;top:88px;font-size:12px;line-height:1.3}
.contact div{display:flex;gap:12px;margin-bottom:10px}
.subscribe-text{left:800px;top:90px;width:220px;font-size:11.5px;line-height:1.3}
.subscribe{left:798px;top:142px;display:flex}
.subscribe .input{width:165px;height:30px;background:var(--white);color:#aaa;font-size:11px;padding:9px 8px}
.subscribe .send{width:45px;height:30px;background:var(--red);display:flex;align-items:center;justify-content:center}
.footer .rule{left:190px;top:206px;width:820px;height:2px;background:var(--white)}
.footer .copy{left:190px;top:218px;font-size:11.5px}
.footer .legal{right:190px;top:218px;font-size:11.5px}
</style>
</head>
<body>

<div class="abs topbar">
  <div class="abs addr">
    <svg width="10" height="14" viewBox="0 0 10 14"><path d="M5 0a5 5 0 0 0-5 5c0 4 5 9 5 9s5-5 5-9a5 5 0 0 0-5-5zm0 7a2 2 0 1 1 0-4 2 2 0 0 1 0 4z" fill="#fff"/></svg>
    14 Lantern Lane Harbourville, HV 20418
  </div>
  <div class="abs phone">
    <svg width="14" height="14" viewBox="0 0 24 24"><path d="M6.6 10.8a15 15 0 0 0 6.6 6.6l2.2-2.2a1 1 0 0 1 1-.25 11.4 11.4 0 0 0 3.6.57 1 1 0 0 1 1 1V20a1 1 0 0 1-1 1A17 17 0 0 1 3 4a1 1 0 0 1 1-1h3.5a1 1 0 0 1 1 1c0 1.25.2 2.45.57 3.57a1 1 0 0 1-.25 1z" fill="#fff"/></svg>
    +000-555-0142
  </div>
</div>

<header class="abs header">
  <div class="abs logo">Italian Restaurant</div>
  <nav class="abs nav">
    <span>Home</span><span>Menu ▾</span><span>Resrevation</span><span>Blogs</span><span>Contact</span>
  </nav>
</header>

<section class="abs hero" role="img" aria-label="Dimly lit restaurant dining room with a chandelier and set tables">
  <div class="abs welcome display">
    <div class="small">Welcome to</div>
    <div class="big">Italian Resturent</div>
  </div>
  <div class="abs booking">
    <h2 class="display">Book a Table</h2>
    <p>Lorem Ipsum is simply dummy text of the printing and typesetting industry.</p>
    <div class="fields">
      <div class="field">Name</div>
      <div class="field">Email</div>
      <div class="field">Phone Number</div>
      <div class="field" style="padding-left:0"><span class="lbl" style="padding-left:14px;width:58px">Date</span>6.19.2018</div>
      <div class="field" style="padding-left:0"><span class="lbl" style="padding-left:14px;width:58px">Time</span>8.00 PM</div>
    </div>
    <div class="btn-request display">Request Booking</div>
  </div>
</section>

<div class="abs section-title display" style="top:730px">Menu</div>

<svg class="abs arrow" style="left:134px" width="20" height="24" viewBox="0 0 20 24"><path d="M16 2 6 12l10 10" fill="none" stroke="#000" stroke-width="5"/></svg>
<svg class="abs arrow" style="left:1043px" width="20" height="24" viewBox="0 0 20 24"><path d="M4 2l10 10L4 22" fill="none" stroke="#ee1100" stroke-width="5"/></svg>

<article class="abs dish" style="left:190px;width:263px">
  <div class="plate" role="img" aria-label="Pizza with assorted toppings" style="background:radial-gradient(circle,#d9903a 0%,#b5552a 60%,#c78a45 100%)"></div>
  <h3 class="display">Pizza</h3>
  <p>Lorem Ipsum is simply dummy text of the printing and typesetting industry.</p>
</article>
<article class="abs dish active" style="left:469px;width:260px">
  <div class="plate" role="img" aria-label="Plate of spaghetti with tomato sauce" style="background:radial-gradient(circle,#c8200f 0%,#e39a3a 45%,#f3f3f3 75%);border-color:#f3f3f3"></div>
  <h3 class="display">Pasta</h3>
  <p>Lorem Ipsum is simply dummy text of the printing and typesetting industry.</p>
</article>
<article class="abs dish" style="left:747px;width:263px">
  <div class="plate" role="img" aria-label="Slice of lasagna on a white plate" style="background:radial-gradient(circle,#e0a040 0%,#d8a050 30%,#f4f4f4 55%)"></div>
  <h3 class="display">Lasagna</h3>
  <p>Lorem Ipsum is simply dummy text of the printing and typesetting industry.</p>
</article>

<section class="abs offer">
  <h2 class="display">We offer the best meal<br>at the best value</h2>
  <p>Lorem Ipsum is simply dummy text of the printing and typesetting industry.</p>
  <div class="btn-red">Book a Table</div>
</section>

<div class="abs section-title display" style="top:1620px">Blogs</div>

<article class="abs post" style="left:190px">
  <div class="photo" role="img" aria-label="Fresh salad on a wooden table" style="background:linear-gradient(135deg,#6b4428,#8fae4a,#5a3a22)"></div>
  <div class="body">
    <h3 class="display">Blog 1</h3>
    <div class="meta"><span>▦ 19.6.2018</span><span>◯ 12 Comments</span></div>
    <p>Lorem Ipsum is simply dummy text of the printing and typesetting industry.</p>
    <div class="more">READ MORE...</div>
  </div>
</article>
<article class="abs post" style="left:469px;width:260px">
  <div class="photo" role="img" aria-label="Spaghetti with meatballs" style="background:linear-gradient(135deg,#4a4a4a,#c27a3a,#7a2a15)"></div>
  <div class="body">
    <h3 class="display">Blog 2</h3>
    <div class="meta"><span>▦ 19.6.2018</span><span>◯ 12 Comments</span></div>
    <p>Lorem Ipsum is simply dummy text of the printing and typesetting industry.</p>
    <div class="more">READ MORE...</div>
  </div>
</article>
<article class="abs post" style="left:747px">
  <div class="photo" role="img" aria-label="Table spread with pasta dishes and fresh ingredients" style="background:linear-gradient(135deg,#3a2a20,#c9b9a0,#8a3020)"></div>
  <div class="body">
    <h3 class="display">Blog 3</h3>
    <div class="meta"><span>▦ 19.6.2018</span><span>◯ 12 Comments</span></div>
    <p>Lorem Ipsum is simply dummy text of the printing and typesetting industry.</p>
    <div class="more">READ MORE...</div>
  </div>
</article>

<div class="abs btn-red view-more">View More</div>

<footer class="abs footer">
  <div class="abs logo">Italian Restaurant</div>
  <div class="abs about">Lorem Ipsum is simply dummy text of the printing and typesetting industry.</div>
  <div class="abs more">READ MORE...</div>
  <div class="abs socials"><span></span><span></span><span></span><span></span></div>

  <h4 class="abs" style="left:474px">Quick Link</h4>
  <div class="abs links">Home<br>Menu<br>Resrevation<br>Blogs<br>Contact</div>

  <h4 class="abs" style="left:601px">Quick Link</h4>
  <div class="abs contact">
    <div><svg width="10" height="14" viewBox="0 0 10 14"><path d="M5 0a5 5 0 0 0-5 5c0 4 5 9 5 9s5-5 5-9a5 5 0 0 0-5-5zm0 7a2 2 0 1 1 0-4 2 2 0 0 1 0 4z" fill="#fff"/></svg><span>14 Lantern Lane Harbourville,<br>HV 20418</span></div>
    <div><svg width="13" height="13" viewBox="0 0 24 24"><path d="M6.6 10.8a15 15 0 0 0 6.6 6.6l2.2-2.2a1 1 0 0 1 1-.25 11.4 11.4 0 0 0 3.6.57 1 1 0 0 1 1 1V20a1 1 0 0 1-1 1A17 17 0 0 1 3 4a1 1 0 0 1 1-1h3.5a1 1 0 0 1 1 1c0 1.25.2 2.45.57 3.57a1 1 0 0 1-.25 1z" fill="#fff"/></svg><span>+000-555-0142</span></div>
    <div><svg width="14" height="11" viewBox="0 0 14 11"><rect x="0.5" y="0.5" width="13" height="10" fill="none" stroke="#fff"/><path d="M.5.5 7 6l6.5-5.5" fill="none" stroke="#fff"/></svg><span>hello@trattoriastandin.test</span></div>
  </div>

  <h4 class="abs" style="left:800px">Subscribe</h4>
  <div class="abs subscribe-text">Lorem Ipsum is simply dummy text of the printing and typesetting industry.</div>
  <div class="abs subscribe">
    <div class="input">Email Address</div>
    <div class="send"><svg width="16" height="16" viewBox="0 0 16 16"><path d="M15 1 1 7l5 2 2 6z" fill="#fff"/></svg></div>
  </div>

  <div class="abs rule"></div>
  <div class="abs copy">© Copyright 2018 Italian Resrurent - All Right Reserved</div>
  <div class="abs legal">Privacy Policy - Terms &amp; conditions</div>
</footer>

</body>
</html>
```